Postcard/Poster design for Feature film

I'm just wrapping post-production on my indie first feature, and I'm going to be attending some big festivals over the next few months to promote my film by handing out postcards.

I'll also be needing posters for festivals that I'll get into.

The name of my film is Salt Hours, and it's a melancholic drama about one woman's desperate need for a male child.
I have a still photo from the film that I'd like to use on the poster and postcard.

The postcard design should take into consideration the fact that a postcard has two sides. All the info doesnt have to on the front. Therefore the post card design should be two designs, the front and the back.
Take a look at a real postcard for inspiration.

Target Market(s)

The arthouse film loving types.

Requirements
Must have
• The design must have the still photo from the film, the name of the film, Salt Hours, and all the other logo's at the bottom.
There are other logos that I'm unable to attach because I reached the limit, but I can send those later.

The postcard design should take into consideration the fact that a postcard has two sides. All the info doesn't have to be on the front of the card. Therefore the post card design should be in two parts, the front and the back.

The postcard size is standard (4 x 6 inches).
Poster 40 inches (wide) x 30 inches (high).

The design must be 350dpi.

```html
<!DOCTYPE html>
<html lang="en">
<head>
<meta charset="utf-8">
<title>Salt Hours — Poster and Postcard</title>
<link href="https://fonts.googleapis.com/css2?family=Great+Vibes&family=Poiret+One&family=Oswald:wght@400&display=swap" rel="stylesheet">
<style>
:root{
  --page:#ffffff;
  --ink:#000000;
  --text:#ffffff;
  --muted:#d9d9d9;
  --light-gold:#d2a24a;
  --gold:#a87a2c;
  --skin:#4a2a14;
  --door:#3b2812;
  --fabric:#7d6a24;
  --top-orange:#e0582c;
  --olive:#2a3314;
  --deep:#0c1006;
  --accent:#e08a14;
}
*{margin:0;padding:0;box-sizing:border-box}
html,body{width:1200px;height:1195px;overflow:hidden;background:var(--page)}
.sheet{position:relative;width:1200px;height:1195px}
.poster,.card-front,.card-back{position:absolute;background:var(--ink);overflow:hidden}
.poster{left:40px;top:27px;width:1060px;height:796px}
.card-front{left:71px;top:853px;width:469px;height:314px}
.card-back{left:593px;top:857px;width:466px;height:310px}

.still{position:absolute;left:0;top:0}
.still-tones{background:
  linear-gradient(180deg,rgba(0,0,0,0) 72%,#000 100%),
  radial-gradient(ellipse 22% 26% at 46% 62%,var(--top-orange) 0%,rgba(224,88,44,.55) 55%,rgba(224,88,44,0) 100%),
  radial-gradient(ellipse 20% 30% at 31% 30%,var(--skin) 0%,rgba(74,42,20,.6) 60%,rgba(74,42,20,0) 100%),
  radial-gradient(ellipse 22% 30% at 16% 78%,var(--fabric) 0%,rgba(125,106,36,.5) 60%,rgba(125,106,36,0) 100%),
  radial-gradient(ellipse 18% 40% at 58% 30%,var(--door) 0%,rgba(59,40,18,0) 100%),
  radial-gradient(ellipse 26% 34% at 6% 14%,var(--light-gold) 0%,rgba(210,162,74,0) 100%),
  linear-gradient(90deg,var(--gold) 0%,#5c4018 22%,#3a2a12 45%,var(--olive) 68%,var(--deep) 100%)}
.poster .still{width:100%;height:620px}
.card-front .still{width:100%;height:280px}
.card-front .still::after{content:"";position:absolute;inset:0;background:linear-gradient(90deg,rgba(0,0,0,0) 45%,#000 75%)}
.card-back .still{top:60px;width:240px;height:250px;opacity:.22}

.title{position:absolute;left:0;top:0;color:var(--text);line-height:1;font-weight:400}
.title span{position:absolute;white-space:nowrap}
.title .initial{font-family:'Great Vibes',cursive}
.title .small,.title .large{font-family:'Poiret One',sans-serif}
.poster .initial{left:470px;top:70px;font-size:160px}
.poster .small{left:690px;top:172px;font-size:46px}
.poster .large{left:600px;top:220px;font-size:120px}
.card-front .initial{left:280px;top:158px;font-size:76px}
.card-front .small{left:352px;top:200px;font-size:22px}
.card-front .large{left:335px;top:222px;font-size:44px}
.card-back .initial{left:42px;top:14px;font-size:72px}
.card-back .small{left:112px;top:56px;font-size:21px}
.card-back .large{left:100px;top:78px;font-size:40px}

.credits{position:absolute;left:150px;top:594px;width:770px;color:var(--text);font-family:'Oswald',sans-serif;font-size:13.5px;line-height:27px;text-align:center}
.credits .role{font-size:7.5px;color:var(--muted);margin:0 3px}
.sponsors{position:absolute;left:150px;top:722px;width:800px;height:56px;display:flex;align-items:center;justify-content:space-between}
.sponsor{display:flex;align-items:center;gap:8px;color:var(--text);font-family:'Oswald',sans-serif;font-size:17px;white-space:nowrap}
.sponsor .mark{width:14px;height:14px;background:var(--text)}
.sponsor.accent{color:var(--accent)}
.sponsor.accent .mark{background:var(--accent)}

.back-credits{position:absolute;left:200px;top:26px;width:250px;color:var(--muted);font-family:'Poiret One',sans-serif;font-size:9px;line-height:11.5px;text-align:center}
.back-credits p{margin-bottom:11px}
</style>
</head>
<body>
<div class="sheet">
  <section class="poster">
    <div class="still still-tones" role="img" aria-label="Film still: a woman in an orange top sits in a warm-lit room by a wooden door, a child's arm around her neck"></div>
    <h1 class="title"><span class="initial">S</span><span class="small">alt</span><span class="large">Hours</span></h1>
    <p class="credits">
      <span class="role">Film Title</span>Salt Hours<span class="role">Production Company</span>Quiet Harbor Productions<span class="role">Producer</span>Nneka Obiora<span class="role">Producer</span>Tobi Adeyemi<span class="role">Director/Writer</span>Nneka Obiora<span class="role">Executive producer</span>Amara Okafor<span class="role">Executive producers</span>
      Efe Odiri, Chioma Odiri, Kunle Odiri, Lola Odiri<span class="role">Executive producers</span>Femi Balogun, Ada Whyte, Seyi Whyte<span class="role">Cinematographer</span>Marta Kowalczyk<span class="role">Production Designer</span>Kofi Mensah Ansah<span class="role">Edited by</span>Paul Verrier<span class="role">Original Music by</span>Jonas Wendler
    </p>
    <div class="sponsors">
      <span class="sponsor"><span class="mark"></span>Lumen Optics</span>
      <span class="sponsor">Chromaline</span>
      <span class="sponsor">Atelier Résidence</span>
      <span class="sponsor">Darkroom Pictures</span>
      <span class="sponsor accent"><span class="mark"></span>Quiet Harbor Productions</span>
    </div>
  </section>

  <section class="card-front">
    <div class="still still-tones" role="img" aria-label="Film still: a woman in an orange top seated in a dim room, a child's arm around her"></div>
    <h2 class="title"><span class="initial">S</span><span class="small">alt</span><span class="large">Hours</span></h2>
  </section>

  <section class="card-back">
    <div class="still still-tones" role="img" aria-label="Faded film still of the woman seated in the dim room"></div>
    <h2 class="title"><span class="initial">S</span><span class="small">alt</span><span class="large">Hours</span></h2>
    <div class="back-credits">
      <p>Film Title – Salt Hours</p>
      <p>Production Company – Quiet Harbor Productions<br>Producer – Nneka Obiora<br>Producer – Tobi Adeyemi</p>
      <p>Director/Writer – Nneka Obiora</p>
      <p>Executive producer – Amara Okafor<br>Executive producers – Efe Odiri, Chioma Odiri, Kunle Odiri, Lola Odiri<br>Executive producers – Femi Balogun, Ada Whyte, Seyi Whyte</p>
      <p>Cinematographer – Marta Kowalczyk<br>Production Designer – Kofi Mensah Ansah<br>Edited by – Paul Verrier<br>Original Music by – Jonas Wendler</p>
    </div>
  </section>
</div>
</body>
</html>
```